Business card design needed

We are a boutique law firm within the Melbourne CBD.

You will need to upload our company logo which is to go on the left hand side of the business card - we then have a Bar Collegium of Tarnwell logo to go perhaps on the bottom right hand side (color)

On the back we would like the website details

www.marlowessolicitors.com.au - with a small logo
Updates

Thank you designers for all your great submissions.  Just going through the designs and we will choose one within the next couple of days.

Kind Regards
Marlowes Solicitors Pty Ltd

Industry/Entity Type

Boutique

Contact Information for Business Card

Dermot Marlowe
Principal
Level 6, 47 Quarry Lane
Melbourne VIC Australia 3000
T+61 3 9620 2088 F+61 3 9629 3938
dermot@marlowessolicitors.com.au
M 0491 570 156

```html
<!DOCTYPE html>
<html lang="en">
<head>
<meta charset="utf-8">
<title>Marlowes Solicitors – Business Card</title>
<link rel="stylesheet" href="https://fonts.googleapis.com/css2?family=Source+Sans+3:wght@300;700&display=swap">
<style>
  :root {
    --card-dark: #3a3a3c;
    --paper: #ffffff;
    --ink-light: #ffffff;
  }
  html, body {
    margin: 0;
    padding: 0;
    width: 1200px;
    height: 741px;
    overflow: hidden;
    background: var(--paper);
  }
  .card {
    position: relative;
    width: 1200px;
    height: 741px;
    background: var(--paper);
    font-family: "Source Sans 3", sans-serif;
  }
  .card-panel {
    position: absolute;
    left: 36px;
    top: 55px;
    width: 1134px;
    height: 644px;
    background: var(--card-dark);
  }
  .divider-vertical {
    position: absolute;
    left: 312px;
    top: 55px;
    width: 6px;
    height: 644px;
    background: var(--paper);
  }
  .divider-horizontal {
    position: absolute;
    left: 175px;
    top: 267px;
    width: 995px;
    height: 5px;
    background: var(--paper);
  }
  .firm-name {
    position: absolute;
    left: 332px;
    top: 136px;
    margin: 0;
    font-weight: 700;
    font-size: 68px;
    line-height: 1;
    color: var(--ink-light);
  }
  .contact {
    position: absolute;
    left: 339px;
    top: 0;
    margin: 0;
    padding: 0;
    list-style: none;
    color: var(--ink-light);
    font-weight: 300;
    font-size: 33px;
    letter-spacing: -0.4px;
  }
  .contact li {
    position: absolute;
    left: 0;
    white-space: nowrap;
    line-height: 1;
  }
  .contact .line-name    { top: 302px; }
  .contact .line-address { top: 366px; }
  .contact .line-phones  { top: 429px; }
  .contact .line-email   { top: 494px; }
  .contact .line-mobile  { top: 558px; }
  .contact .fax {
    position: absolute;
    left: 302px;
  }
</style>
</head>
<body>
  <main class="card">
    <div class="card-panel"></div>
    <div class="divider-vertical"></div>
    <div class="divider-horizontal"></div>

    <h1 class="firm-name">Marlowes</h1>

    <ul class="contact">
      <li class="line-name">Dermot Marlowe Principal Marlowes Solicitors Pty Ltd</li>
      <li class="line-address">Level 6, 47 Quarry Lane Melbourne VIC Australia 3000</li>
      <li class="line-phones"><span class="tel">T: +61 3 9555 0147</span><span class="fax">F: +61 3 9555 0382</span></li>
      <li class="line-email">E: dermot@marlowessolicitors.com.au</li>
      <li class="line-mobile">M:&nbsp; 0491 570 156</li>
    </ul>
  </main>
</body>
</html>
```